Brightwater Medical business cards

Double sided business cards.

Medical technology consulting company.

Business cards with two names on the front, upper to middle left:

Dr Colin R. Haskell MBBS FRACP +61491578204
Dr Paul Brennagh PhD MBusLaw +61472019847

Email and website addresses bottom right:

colin@brightwatermedical.com.au
www.brightwatermedical.com.au

Tree logo (as per attached file) on front in a suitable position.

Tag line (as per attached files) on the back.

Need a file format to upload to Desk Ford or Cardmoor.

```html
<!DOCTYPE html>
<html lang="en">
<head>
<meta charset="utf-8">
<title>Brightwater Medical – Business Cards</title>
<link rel="stylesheet" href="https://fonts.googleapis.com/css2?family=Montserrat:wght@400;500;600;700&display=swap">
<style>
  :root {
    --bg: #e9eaea;
    --brand-green: #3db54a;
    --pattern-green: #43a83c;
    --pattern-light: #6cc04a;
    --ink-brown: #3a1d1d;
    --ink-grey: #4a4a4a;
    --card-white: #ffffff;
    --rule: #5a3a3a;
  }
  * { box-sizing: border-box; margin: 0; padding: 0; }
  html, body { width: 1200px; height: 800px; overflow: hidden; }
  body {
    background: var(--bg);
    font-family: "Montserrat", sans-serif;
    position: relative;
  }
  .card {
    position: absolute;
    top: 251px;
    width: 520px;
    height: 297px;
    box-shadow: 0 6px 18px rgba(0,0,0,0.18);
  }
  .card-back {
    left: 60px;
    background: radial-gradient(circle at 40% 45%, var(--pattern-light), var(--pattern-green));
  }
  .card-front {
    left: 620px;
    background: var(--card-white);
  }
  .brand {
    position: absolute;
    right: 28px;
    top: 52px;
    text-align: right;
  }
  .brand-name {
    display: flex;
    align-items: center;
    justify-content: flex-end;
    gap: 8px;
    font-size: 19px;
    font-weight: 500;
    color: var(--brand-green);
    letter-spacing: 0.3px;
  }
  .brand-dot {
    width: 14px; height: 14px;
    border-radius: 50%;
    background: var(--brand-green);
  }
  .brand-tagline {
    margin-top: 5px;
    font-size: 8.5px;
    font-weight: 500;
    color: var(--brand-green);
  }
  .brand-rule {
    position: absolute;
    right: 28px;
    top: 112px;
    width: 210px;
    border-top: 1px solid var(--rule);
  }
  .person {
    position: absolute;
    left: 30px;
  }
  .person-1 { top: 92px; }
  .person-2 { top: 152px; }
  .person-name {
    font-size: 14px;
    font-weight: 700;
    color: var(--brand-green);
  }
  .person-credentials {
    margin-top: 2px;
    font-size: 10.5px;
    font-weight: 500;
    color: var(--ink-brown);
  }
  .contact-line {
    display: flex;
    align-items: center;
    gap: 7px;
    margin-top: 3px;
    font-size: 11.5px;
    color: var(--ink-grey);
  }
  .contact-line svg { width: 11px; height: 11px; flex: none; }
  .contact-rule {
    position: absolute;
    left: 30px;
    top: 216px;
    width: 200px;
    border-top: 1px solid var(--rule);
  }
  .contact-block {
    position: absolute;
    left: 30px;
    top: 224px;
  }
  .contact-block .contact-line { margin-top: 5px; font-size: 12px; }
</style>
</head>
<body>
  <section class="card card-back" role="img" aria-label="Repeating embossed tree pattern in green with one highlighted white tree"></section>

  <section class="card card-front">
    <div class="brand">
      <div class="brand-name"><span class="brand-dot"></span>BRIGHTWATER MEDICAL</div>
      <div class="brand-tagline">Vision | Validation | Launch</div>
    </div>
    <div class="brand-rule"></div>

    <div class="person person-1">
      <div class="person-name">Dr Colin R. Haskell</div>
      <div class="person-credentials">MBBS FRACP</div>
      <div class="contact-line">
        <svg viewBox="0 0 12 12"><path fill="#3db54a" d="M1 4c0-2 2-3 5-3s5 1 5 3l-2 1-1-1.5H4L3 5zM3 6h6l1 5H2z"/></svg>
        +61491578204
      </div>
    </div>

    <div class="person person-2">
      <div class="person-name">Dr Paul Brennagh</div>
      <div class="person-credentials">PhD MBusLaw</div>
      <div class="contact-line">
        <svg viewBox="0 0 12 12"><path fill="#3db54a" d="M1 4c0-2 2-3 5-3s5 1 5 3l-2 1-1-1.5H4L3 5zM3 6h6l1 5H2z"/></svg>
        +61472019847
      </div>
    </div>

    <div class="contact-rule"></div>
    <div class="contact-block">
      <div class="contact-line">
        <svg viewBox="0 0 12 12"><rect x="1" y="3" width="10" height="7" rx="1" fill="#3db54a"/><path d="M1.5 3.5 6 7l4.5-3.5" stroke="#fff" fill="none"/></svg>
        colin@brightwatermedical.com.au
      </div>
      <div class="contact-line">
        <svg viewBox="0 0 12 12"><circle cx="6" cy="6" r="5" fill="none" stroke="#3db54a" stroke-width="1.4"/><path d="M1 6h10M6 1c-2.5 3-2.5 7 0 10M6 1c2.5 3 2.5 7 0 10" stroke="#3db54a" fill="none"/></svg>
        www.brightwatermedical.com.au
      </div>
    </div>
  </section>
</body>
</html>
```